IT Consulting company Needs a Logo Design and Business Cards

I need a New Logo and Business Cards for an established IT Managed Services Company that specializes in flat-rate managed IT services. We provide Design and Build, Help Desk, Onsite and Remote Support Services.

Target Market(s)

Corporate Clients

Industry/Entity Type

It Company

Logo Text

Halbrook Computer Group

Requirements
Nice to have
• Tag Line= Technology at Lightning Speed

```html
<!DOCTYPE html>
<html lang="en">
<head>
<meta charset="utf-8">
<title>Halbrook Computer Group – Business Cards</title>
<link href="https://fonts.googleapis.com/css2?family=Oswald:wght@300;400&display=swap" rel="stylesheet">
<style>
  :root{
    --backdrop:#2e2f2e;
    --frame:#05080a;
    --drop:#6f6d6e;
    --card:#e4e5e6;
    --card-light:#e9eae9;
    --green:#0d8a43;
    --green-soft:#72c594;
    --ink:#111111;
  }
  html,body{margin:0;padding:0;width:1200px;height:1200px;overflow:hidden;background:var(--backdrop);}
  .board{position:absolute;left:0;top:0;width:1500px;height:1500px;transform:scale(.8);transform-origin:0 0;font-family:'Oswald',sans-serif;font-weight:300;}
  .abs{position:absolute;}
  .frame{background:var(--frame);}
  .drop{background:var(--drop);}
  .card{background:linear-gradient(90deg,var(--card-light),var(--card));overflow:hidden;}
  .chevrons{position:absolute;left:0;top:0;}
  .vision{position:absolute;color:var(--ink);font-size:43px;line-height:54px;margin:0;white-space:nowrap;}
  .brand-name{position:absolute;color:var(--green);font-weight:300;white-space:nowrap;margin:0;}
  .brand-dot{position:absolute;border-radius:50%;background:var(--green);}
  .web-line{position:absolute;color:var(--green);font-size:43px;display:flex;align-items:center;gap:8px;white-space:nowrap;}
  .tagline{position:absolute;color:var(--green);font-size:19.5px;white-space:nowrap;}
  .contact{position:absolute;display:flex;align-items:center;}
  .contact-icon{width:62px;height:62px;border-radius:50%;background:var(--green-soft);display:flex;align-items:center;justify-content:center;}
  .contact-text{color:var(--green);font-size:29px;margin-left:19px;white-space:nowrap;}
  .divider{position:absolute;width:67px;height:3px;background:var(--green-soft);}
</style>
</head>
<body>
<div class="board">

  <!-- Front card -->
  <div class="abs frame" style="left:17px;top:49px;width:1053px;height:729px;"></div>
  <div class="abs drop" style="left:52px;top:138px;width:1007px;height:604px;"></div>
  <section class="abs card front-card" style="left:33px;top:118px;width:1006px;height:603px;">
    <svg class="chevrons" width="1006" height="603" viewBox="0 0 1006 603" aria-hidden="true">
      <polygon points="305,0 382,0 510,257 487,305 350,104" fill="var(--green-soft)"/>
      <polygon points="350,104 399,72 524,374 410,603 305,603 430,302" fill="var(--green)"/>
    </svg>
    <p class="vision" style="left:46px;top:216px;">put a picture of your<br>group activity in here<br>or the company's<br>vision and mission</p>
    <div class="brand-dot" style="left:651px;top:110px;width:190px;height:190px;"></div>
    <p class="brand-name" style="left:622px;top:390px;font-size:30px;">Halbrook Computer Group</p>
    <div class="web-line" style="left:592px;top:498px;">
      <svg width="36" height="36" viewBox="0 0 36 36" aria-hidden="true">
        <circle cx="17" cy="17" r="14" fill="none" stroke="var(--green)" stroke-width="3"/>
        <path d="M4 14 Q17 22 30 12 M10 5 Q20 16 14 31" fill="none" stroke="var(--green)" stroke-width="2.5"/>
        <path d="M22 22 L32 27 L27 28 L25 33 Z" fill="var(--green)"/>
      </svg>
      <span>urwebsitename.com</span>
    </div>
  </section>

  <!-- Brand panel -->
  <div class="brand-dot" style="left:1180px;top:215px;width:210px;height:210px;"></div>
  <p class="brand-name" style="left:1117px;top:502px;font-size:40px;">Halbrook Computer Group</p>

  <!-- Back card -->
  <div class="abs frame" style="left:366px;top:725px;width:1100px;height:720px;"></div>
  <div class="abs drop" style="left:388px;top:808px;width:1014px;height:605px;"></div>
  <section class="abs card back-card" style="left:410px;top:779px;width:1022px;height:613px;">
    <svg class="chevrons" width="1022" height="613" viewBox="0 0 1022 613" aria-hidden="true">
      <polygon points="470,281 585,541 638,506 688,613 578,613 436,356" fill="var(--green)"/>
      <polygon points="578,0 688,0 550,309 638,506 585,541 448,231" fill="var(--green-soft)"/>
    </svg>
    <div class="brand-dot" style="left:120px;top:60px;width:105px;height:105px;"></div>
    <p class="brand-name" style="left:240px;top:72px;font-size:24px;">Halbrook Computer Group</p>
    <span class="tagline" style="left:240px;top:112px;">Technology at Lightning Speed</span>

    <div class="contact" style="left:91px;top:202px;">
      <div class="contact-icon">
        <svg width="38" height="34" viewBox="0 0 38 34" aria-hidden="true">
          <path d="M19 2 L2 17 L7 17 L7 32 L15 32 L15 22 L23 22 L23 32 L31 32 L31 17 L36 17 Z" fill="var(--green)"/>
        </svg>
      </div>
      <span class="contact-text">Street Address Here</span>
    </div>
    <div class="divider" style="left:170px;top:281px;"></div>

    <div class="contact" style="left:91px;top:295px;">
      <div class="contact-icon">
        <svg width="36" height="34" viewBox="0 0 36 34" aria-hidden="true">
          <path d="M2 6 L34 19 L16 22 L14 32 L11 20 Z" fill="var(--green)"/>
        </svg>
      </div>
      <span class="contact-text">urname@email.com</span>
    </div>
    <div class="divider" style="left:170px;top:369px;"></div>

    <div class="contact" style="left:91px;top:387px;">
      <div class="contact-icon">
        <svg width="38" height="34" viewBox="0 0 38 34" aria-hidden="true">
          <path d="M3 11 Q19 0 35 11 L31 16 L25 13 L25 9 Q19 7 13 9 L13 13 L7 16 Z" fill="var(--green)"/>
          <rect x="6" y="17" width="26" height="15" rx="3" fill="var(--green)"/>
          <circle cx="19" cy="24" r="4" fill="var(--green-soft)"/>
        </svg>
      </div>
      <span class="contact-text" style="margin-left:23px;">YOUR PHONE</span>
    </div>
    <div class="divider" style="left:170px;top:476px;"></div>

    <div class="contact" style="left:70px;top:488px;">
      <div class="contact-icon">
        <svg width="36" height="36" viewBox="0 0 36 36" aria-hidden="true">
          <circle cx="18" cy="18" r="15" fill="var(--green)"/>
          <path d="M5 14 Q18 22 31 12 M11 5 Q22 17 15 32 M22 4 Q14 18 28 30" fill="none" stroke="var(--green-soft)" stroke-width="2"/>
        </svg>
      </div>
      <span class="contact-text" style="margin-left:22px;font-size:28px;">www.websitename.com</span>
    </div>

    <p class="vision" style="left:675px;top:226px;">put a picture of your<br>group activity in here<br>or the company's<br>vision and mission</p>
  </section>

</div>
</body>
</html>
```